Professional Services/Construction Management (Millwork) Biz Cards

We've decided on a logo and have our color palette set, now we want to design some very professional looking cards that make a strong first impression - they'll reflect our tagline (that we're going to put on the back: Innovative. Professional. Leaders.

The example business card shows generally the direction we've been thinking of going for the back side - **but we're open to other ideas**

Target Market(s)

The cards should target more high-end (wealthy) owners and general contracting companies. We want them to convey a strong first impression - in a professional and not garish way.

Industry/Entity Type

Construction Company

Contact Information for Business Card

There needs to be a place for our company contractor's license number and business address. We want to also have people's names, titles, phone number, email address. The back can be the logo, tagline and web address

Requirements
Must have
• follow our color palette
Nice to have
• Font & Styles should compliment the Harrow Joinery fonts, but not necessarily match exactly

```html
<!DOCTYPE html>
<html lang="en">
<head>
<meta charset="utf-8">
<title>Harrow Joinery — Business Cards</title>
<link rel="stylesheet" href="https://fonts.googleapis.com/css2?family=Open+Sans:wght@400;600;700&display=swap">
<style>
  :root {
    --bg: #ecebe8;
    --paper: #ffffff;
    --umber: #7b6f65;
    --mauve: #cbb8b9;
    --leaf: #6bb043;
    --ink: #6a615a;
    --ink-dark: #5a514b;
  }
  * { box-sizing: border-box; margin: 0; padding: 0; }
  html, body { width: 1200px; height: 800px; overflow: hidden; }
  body {
    background: var(--bg);
    font-family: "Open Sans", Arial, sans-serif;
    position: relative;
  }
  .card {
    position: absolute;
    background: var(--paper);
    box-shadow: 0 6px 18px rgba(0,0,0,.18);
    overflow: hidden;
  }

  /* Back of card */
  .card-back { left: 100px; top: 110px; width: 340px; height: 580px; }
  .card-back .band-left { position: absolute; left: 0; top: 0; width: 120px; height: 100%; background: var(--umber); }
  .card-back .band-right { position: absolute; right: 0; top: 0; width: 90px; height: 100%; background: var(--umber); }
  .card-back .brand {
    position: absolute; left: 120px; top: 40px; width: 130px; height: 130px;
    border-radius: 50%; background: var(--mauve);
  }
  .card-back .brand-name {
    position: absolute; left: 170px; top: 48px;
    writing-mode: vertical-rl;
    color: var(--leaf); font-weight: 700; font-size: 22px; letter-spacing: .5px;
  }
  .card-back .tagline {
    position: absolute; left: 196px; top: 200px;
    writing-mode: vertical-rl;
    color: var(--leaf); font-weight: 600; font-size: 19px;
  }
  .card-back .web {
    position: absolute; left: 160px; top: 232px;
    writing-mode: vertical-rl;
    color: var(--ink); font-size: 14px;
  }

  /* Front of card */
  .card-front { left: 520px; top: 225px; width: 600px; height: 350px; }
  .card-front .band { position: absolute; left: 0; top: 0; width: 70px; height: 100%; background: var(--umber); }
  .card-front .license {
    position: absolute; left: 22px; bottom: 24px;
    writing-mode: vertical-rl; transform: rotate(180deg);
    color: #efe9e4; font-size: 11px; letter-spacing: .5px;
  }
  .card-front .brand { position: absolute; left: 30px; top: 22px; width: 84px; height: 84px; border-radius: 50%; background: var(--mauve); }
  .card-front .brand-name {
    position: absolute; left: 124px; top: 52px;
    color: var(--leaf); font-weight: 700; font-size: 14px; letter-spacing: .5px;
  }
  .person { position: absolute; left: 150px; top: 96px; color: var(--ink); }
  .person-name { font-weight: 700; font-size: 24px; letter-spacing: .5px; text-transform: uppercase; color: var(--ink-dark); }
  .person-title { font-size: 16px; margin-top: 2px; }
  .contact { position: absolute; left: 150px; top: 218px; color: var(--ink); font-size: 14px; list-style: none; }
  .contact li { display: flex; align-items: center; gap: 8px; line-height: 22px; }
  .contact .icon { width: 14px; height: 14px; }
  .address { position: absolute; left: 150px; top: 272px; color: var(--ink-dark); font-weight: 700; font-size: 14px; text-transform: uppercase; line-height: 20px; font-style: normal; }
</style>
</head>
<body>
  <section class="card card-back" aria-label="Card back">
    <div class="band-left"></div>
    <div class="band-right"></div>
    <div class="brand" aria-hidden="true"></div>
    <p class="brand-name">Harrow Joinery</p>
    <p class="tagline">Innovative. Professional. Leaders.</p>
    <p class="web">www.HarrowJoinery.com</p>
  </section>

  <section class="card card-front" aria-label="Card front">
    <div class="band"></div>
    <p class="license">Lic. 0123 456789</p>
    <div class="brand" aria-hidden="true"></div>
    <p class="brand-name">Harrow Joinery</p>
    <div class="person">
      <p class="person-name">Grant Ellison</p>
      <p class="person-title">Business Development Manager</p>
    </div>
    <ul class="contact">
      <li>
        <svg class="icon" viewBox="0 0 14 14" aria-hidden="true"><rect width="14" height="14" rx="2" fill="#6bb043"/><path d="M4 3.2c.4-.3.9-.2 1.1.2l.6 1.2c.2.4.1.7-.2 1l-.4.4c.4.9 1.1 1.6 2 2l.4-.4c.3-.3.7-.4 1-.2l1.2.6c.4.2.5.7.2 1.1-.6.9-1.6 1.2-2.6.7C5.6 9 4.5 7.9 3.8 6.2c-.4-1-.3-2.3.2-3z" fill="#fff"/></svg>
        205.555.0148
      </li>
      <li>
        <svg class="icon" viewBox="0 0 14 14" aria-hidden="true"><rect width="14" height="14" rx="2" fill="#6bb043"/><rect x="3" y="4" width="8" height="6" fill="none" stroke="#fff" stroke-width="1"/><path d="M3 4l4 3.2L11 4" fill="none" stroke="#fff" stroke-width="1"/></svg>
        grant@harrowjoinery.com
      </li>
    </ul>
    <address class="address">410 Alder Ridge Road, Suite 120<br>Fairview, AL 35010</address>
  </section>
</body>
</html>
```